Homepage Real Estate Agency

I need a web design for a real estate agency in Luxembourg. A short draft for the front page can be found in the project details. (Page 1+2) The main colors of the site should be blue as shown in the project details. (Page 3)
The main target for this site is to promote real estates and a small presentation of the company.

Industry/Entity Type

Real Estate

Requirements
Must have
• On the front page estates are shown in a short preview in small boxes, on the right side is a search. The search is hidden except for the front page. The header has 4 buttons and the logo of the company.

```html
<!DOCTYPE html>
<html lang="en">
<head>
<meta charset="utf-8">
<title>Real Estate Agency – Home</title>
<link href="https://fonts.googleapis.com/css2?family=Arimo:wght@400;700&family=Ubuntu:wght@500;700&family=Nunito:wght@800;900&display=swap" rel="stylesheet">
<style>
:root{
  --sky:#b4d2dd;
  --sky-dark:#9cc1cf;
  --band:#2c7c99;
  --band-light:#4ea1c0;
  --teal:#3a90b6;
  --orange:#f7931e;
  --orange-dark:#e47c08;
  --slate:#4b5a92;
  --ink:#333;
  --muted:#777;
  --panel:#f2f2f2;
  --line:#c9c9c9;
  --footer-ink:#17384a;
  --white:#fff;
}
*{box-sizing:border-box;margin:0;padding:0}
html,body{width:840px;height:1200px;overflow:hidden}
body{position:relative;font-family:"Arimo",Arial,sans-serif;color:var(--ink);
  background:radial-gradient(ellipse at 30% 20%,#c3dde6 0%,var(--sky) 45%,var(--sky-dark) 100%)}
.abs{position:absolute}
/* header */
.call{left:505px;top:10px;display:flex;align-items:center;gap:8px;color:var(--white);font:700 21px "Ubuntu",sans-serif}
.call b{font-size:24px}
.call-icon{width:22px;height:22px;background:var(--orange);border-radius:4px;display:flex;align-items:center;justify-content:center}
.nav a{position:absolute;top:52px;color:var(--white);font:700 16px "Ubuntu",sans-serif;text-decoration:none}
/* slider */
.slider{left:121px;top:84px;width:600px;height:299px;background:var(--white);padding:6px;box-shadow:0 2px 6px rgba(0,0,0,.25)}
.slide{position:relative;width:100%;height:100%;overflow:hidden;background:linear-gradient(90deg,#f4f4f4 0%,#e6e6e6 45%,#d8d8d8 100%)}
.slide-photo{position:absolute;left:235px;top:0;right:0;bottom:10px;
  background:linear-gradient(90deg,rgba(230,230,230,1) 0%,rgba(140,160,190,.6) 25%,#7f92b8 55%,#5d6f98 80%,#51623a 100%)}
.slide-title{position:absolute;left:57px;top:20px;width:420px;font:900 29px/36px "Nunito",sans-serif;color:var(--slate)}
.slide-text{position:absolute;left:63px;top:98px;width:230px;font-size:13.5px;line-height:16.5px;color:#555}
.btn{display:flex;align-items:center;justify-content:center;background:linear-gradient(#fba73c,var(--orange-dark));color:var(--white);font:700 13px "Arimo",sans-serif}
.more{position:absolute;left:189px;top:214px;width:120px;height:34px;font-size:19px}
.arrow{position:absolute;top:124px}
.badge-new{position:absolute;right:0;top:0}
.dots{left:639px;top:390px;display:flex;gap:6px}
.dots span{width:12px;height:12px;border-radius:50%;background:#e8f0f3;border:1px solid #9ab}
.dots span.on{background:var(--teal)}
/* value search */
.band{left:0;width:840px;background:linear-gradient(var(--band),#1f6580)}
.value-panel{left:109px;top:407px;width:626px;height:84px;background:linear-gradient(var(--band-light),#3688a8);box-shadow:0 2px 4px rgba(0,0,0,.3)}
.value-title{left:131px;top:410px;color:var(--white);font:700 15px "Ubuntu",sans-serif}
.value-sub{left:131px;top:428px;color:#d5eb8a;font:700 9px "Arimo",sans-serif}
.field{background:var(--white);border:1px solid var(--line);color:#aaa;font-size:12px;padding:4px 7px;height:22px}
/* content */
.content{left:120px;top:496px;width:611px;height:497px;background:var(--white)}
.sidebar{left:529px;top:496px;width:202px;height:497px;background:var(--panel);border-left:1px solid #ddd}
.listing-title{color:var(--teal);font:500 15px "Ubuntu",sans-serif}
.listing-title::before{content:"";display:inline-block;border-left:6px solid var(--teal);border-top:4px solid transparent;border-bottom:4px solid transparent;margin-right:5px}
.listing-photo{width:178px;height:116px;border:1px solid var(--line);padding:4px;background:var(--white)}
.listing-photo div{width:100%;height:100%}
.listing-caption{width:180px;font-size:10.5px;line-height:12px;color:#333}
.tab{height:27px;background:linear-gradient(#fafafa,#dcdcdc);box-shadow:0 1px 3px rgba(0,0,0,.25);color:var(--teal);font:500 15px "Ubuntu",sans-serif;padding:5px 9px}
.links{list-style:none;font-size:10.5px;line-height:12px}
.links li::before{content:"";display:inline-block;border-left:6px solid #4a6f86;border-top:4px solid transparent;border-bottom:4px solid transparent;margin-right:5px}
.links a{color:var(--orange-dark)}
.side-label{color:#3b7fa5;font-size:13px}
.side-small{font-size:11px;color:#444;line-height:13px}
.mini{height:19px;font-size:12px}
.track{left:539px;top:705px;width:173px;height:4px;background:linear-gradient(90deg,var(--orange) 0 47%,#ccc 47%)}
.knob{left:617px;top:700px;width:9px;height:13px;background:#ddd;border:1px solid #999;border-radius:2px}
.social{left:542px;top:946px;display:grid;grid-template-columns:90px 90px;gap:8px 0;font:700 12px "Arimo",sans-serif;color:var(--teal)}
.social span{display:flex;align-items:center;gap:5px}
.social i{width:14px;height:14px;background:var(--teal);display:inline-block}
/* partners */
.partners-panel{left:109px;top:995px;width:626px;height:85px;background:linear-gradient(var(--band-light),#3688a8)}
.partner{background:#9a9a9a;border:1px solid #ccc}
/* footer */
.foot h4{position:absolute;top:1097px;color:var(--white);font:500 14px "Ubuntu",sans-serif}
.foot ul{position:absolute;top:1120px;list-style:none;font-size:10.5px;line-height:12px;color:var(--footer-ink)}
</style>
</head>
<body>

<header>
  <div class="call abs"><span class="call-icon"><svg width="14" height="14" viewBox="0 0 24 24"><path fill="#fff" d="M6.6 10.8a15 15 0 006.6 6.6l2.2-2.2c.3-.3.7-.4 1-.2 1.1.4 2.3.6 3.6.6.6 0 1 .4 1 1V20c0 .6-.4 1-1 1A17 17 0 013 4c0-.6.4-1 1-1h3.5c.6 0 1 .4 1 1 0 1.3.2 2.5.6 3.6.1.3 0 .7-.2 1z"/></svg></span>Call Us <b>55501234</b></div>
  <nav class="nav">
    <a style="left:361px" href="#">Home</a>
    <a style="left:441px" href="#">About Us</a>
    <a style="left:544px" href="#">Services</a>
    <a style="left:641px" href="#">Contact Us</a>
  </nav>
</header>

<section class="slider abs">
  <div class="slide">
    <div class="slide-photo" role="img" aria-label="Photo of modern townhouses with balconies under a blue sky"></div>
    <h1 class="slide-title">Sed ut perspiciatis unde omnis iste natus</h1>
    <p class="slide-text">error sit voluptatem accusantium doloremque laudantium, totam rem aperiam, eaque ipsa quae ab illo inventore veritatis et quasi architecto beatae vitae dicta sunt explicabo. Nemo enim ipsam</p>
    <a class="btn more" href="#">More</a>
    <svg class="arrow" style="left:2px" width="34" height="42" viewBox="0 0 34 42"><path d="M28 2 8 21l20 19" fill="none" stroke="#fff" stroke-width="6" opacity=".85"/></svg>
    <svg class="arrow" style="right:4px" width="34" height="42" viewBox="0 0 34 42"><path d="M6 2l20 19L6 40" fill="none" stroke="#fff" stroke-width="6" opacity=".9"/></svg>
    <svg class="badge-new" width="72" height="72" viewBox="0 0 72 72"><path d="M18 0h24l30 30v24z" fill="#7cc242"/><text x="47" y="29" fill="#fff" font-family="Nunito,sans-serif" font-weight="900" font-size="14" transform="rotate(45 47 29)" text-anchor="middle">NEW!</text></svg>
  </div>
</section>
<div class="dots abs"><span></span><span class="on"></span><span></span><span></span><span></span></div>

<section class="home-values">
  <div class="band abs" style="top:416px;height:80px"></div>
  <div class="value-panel abs"></div>
  <h2 class="value-title abs">Get Home Values on 100 Million + Addresses</h2>
  <p class="value-sub abs">Enter the Property Information Below</p>
  <div class="field abs" style="left:148px;top:453px;width:235px">Address</div>
  <div class="field abs" style="left:404px;top:453px;width:171px">City</div>
  <a class="btn abs" style="left:601px;top:452px;width:89px;height:24px;font-size:15px" href="#">Search</a>
</section>

<main>
  <div class="content abs"></div>

  <article class="listing">
    <h3 class="listing-title abs" style="left:132px;top:503px">Buy &amp; Sale (1045)</h3>
    <div class="listing-photo abs" style="left:131px;top:525px"><div role="img" aria-label="Photo of a living room opening onto a sunset terrace" style="background:linear-gradient(135deg,#3b2a1e,#a56a35 50%,#5a7fa8)"></div></div>
    <p class="listing-caption abs" style="left:134px;top:648px">Inside manufactured homesInside manufactured homes</p>
  </article>
  <article class="listing">
    <h3 class="listing-title abs" style="left:336px;top:503px">Apartament (9875)</h3>
    <div class="listing-photo abs" style="left:333px;top:525px"><div role="img" aria-label="Photo of a bright interior with arched windows" style="background:linear-gradient(135deg,#6b5a4a,#d9c7ad 50%,#8c7764)"></div></div>
    <p class="listing-caption abs" style="left:336px;top:648px">Inside manufactured homesInside manufactured homes</p>
  </article>
  <article class="listing">
    <h3 class="listing-title abs" style="left:135px;top:679px">Apartament (9875)</h3>
    <div class="listing-photo abs" style="left:130px;top:703px"><div role="img" aria-label="Photo of a modern glass office building" style="background:linear-gradient(180deg,#c9d3dc,#8a939b 60%,#555c60)"></div></div>
    <p class="listing-caption abs" style="left:131px;top:826px">Inside manufactured homesInside manufactured homes</p>
  </article>
  <article class="listing">
    <h3 class="listing-title abs" style="left:336px;top:679px">Buy &amp; Sale (1045)</h3>
    <div class="listing-photo abs" style="left:333px;top:703px"><div role="img" aria-label="Photo of a family house with a for-sale sign on the lawn" style="background:linear-gradient(180deg,#c7d7e6,#8e98a0 50%,#4f8a3a)"></div></div>
    <p class="listing-caption abs" style="left:334px;top:826px">Inside manufactured homesInside manufactured homes</p>
  </article>

  <section class="articles">
    <h3 class="tab abs" style="left:109px;top:866px;width:403px">Articles &amp; advice</h3>
    <ul class="links abs" style="left:133px;top:921px">
      <li><a href="#">Fastest-growing small towns</a></li>
      <li><a href="#">February gardening checklist</a></li>
      <li><a href="#">Choose a home for the right reasons</a></li>
      <li><a href="#">A bicyclists' house built for two</a></li>
      <li><a href="#">Home staging on the cheap: 9 tips</a></li>
    </ul>
    <ul class="links abs" style="left:336px;top:921px">
      <li><a href="#">Fastest-growing small towns</a></li>
      <li><a href="#">February gardening checklist</a></li>
      <li><a href="#">Choose a home for the right reasons</a></li>
      <li><a href="#">A bicyclists' house built for two</a></li>
      <li><a href="#">Home staging on the cheap: 9 tips</a></li>
    </ul>
  </section>
</main>

<aside>
  <div class="sidebar abs"></div>
  <h3 class="tab abs" style="left:529px;top:513px;width:203px">Search for properties</h3>
  <p class="side-label abs" style="left:539px;top:554px">Now on sale:</p>
  <div class="field abs" style="left:539px;top:573px;width:173px;font-size:11px">City State or Zip</div>
  <a class="btn abs" style="left:648px;top:602px;width:64px;height:19px" href="#">Find</a>
  <p class="side-label abs" style="left:539px;top:634px">Order by:</p>
  <div class="field abs" style="left:600px;top:632px;width:112px;font-size:11px">Lot size<svg style="position:absolute;right:6px;top:7px" width="9" height="6"><path d="M0 0h9L4.5 6z" fill="var(--orange)"/></svg></div>
  <p class="side-label abs" style="left:539px;top:674px">Area Miles</p>
  <div class="field abs mini" style="left:608px;top:673px;width:64px"></div>
  <a class="btn abs" style="left:680px;top:673px;width:32px;height:19px" href="#">All</a>
  <div class="track abs"></div><div class="knob abs"></div>
  <p class="side-label abs" style="left:539px;top:730px">Size</p>
  <div class="field abs mini" style="left:571px;top:729px;width:48px;text-align:right;font-size:11px">3</div>
  <div class="field abs mini" style="left:625px;top:729px;width:48px;text-align:right;font-size:11px">68</div>
  <a class="btn abs" style="left:677px;top:729px;width:35px;height:19px" href="#">All</a>
  <a class="abs" style="left:628px;top:758px;font:700 10.5px Arimo,sans-serif;color:var(--orange-dark);text-decoration:none" href="#">More properties ▸</a>

  <h3 class="tab abs" style="left:529px;top:777px;width:203px">Newsletter</h3>
  <p class="side-small abs" style="left:539px;top:811px;width:175px">going to use a passage of Lorem you need to be sure there i</p>
  <div class="field abs" style="left:539px;top:844px;width:173px;font-size:11px">Email</div>
  <a class="btn abs" style="left:632px;top:876px;width:80px;height:19px" href="#">Subscribe</a>

  <h3 class="tab abs" style="left:529px;top:907px;width:203px">Follow Us</h3>
  <div class="social abs">
    <span><i></i>Linkbook</span><span><i></i>Chirper</span>
    <span><i></i>Circles</span><span><i></i>Blogline</span>
  </div>
</aside>

<section class="partners">
  <div class="band abs" style="top:995px;height:85px"></div>
  <div class="partners-panel abs"></div>
  <h3 class="abs" style="left:129px;top:1003px;color:#fff;font:700 15px Ubuntu,sans-serif">Our Partners</h3>
  <div class="partner abs" style="left:147px;top:1027px;width:140px;height:37px;background:#b8b8b8"></div>
  <div class="partner abs" style="left:297px;top:1027px;width:147px;height:37px;background:#555"></div>
  <div class="partner abs" style="left:453px;top:1009px;width:113px;height:55px;border-radius:50% 50% 6px 6px;background:#6d6d6d"></div>
  <div class="partner abs" style="left:576px;top:1027px;width:101px;height:37px;background:#ededed"></div>
</section>

<footer class="foot">
  <h4 style="left:129px">Menu</h4>
  <ul style="left:129px"><li>About Us</li><li>Services</li><li>Choose a home for the</li><li>A bicyclists' house built for two</li><li>Contact</li></ul>
  <h4 style="left:289px">Category</h4>
  <ul style="left:289px"><li>growing small towns</li><li>February gardening</li><li>Choose a &nbsp;the right reasons</li><li>A bicyclists' house built for two</li><li>Home s 9 tips</li></ul>
  <h4 style="left:449px">Articles</h4>
  <ul style="left:449px"><li>growing small towns</li><li>February gardening</li><li>Choose a &nbsp;the right reasons</li><li>A bicyclists' house built for two</li><li>Home s 9 tips</li></ul>
  <h4 style="left:601px">Contact</h4>
  <ul style="left:601px;top:1117px">
    <li style="font:700 12px Arimo,sans-serif">Call Us 55501234</li>
    <li style="font:700 12px Arimo,sans-serif;margin:3px 0 3px;display:flex;align-items:center;gap:5px"><svg width="22" height="14" viewBox="0 0 22 14"><rect x=".5" y=".5" width="21" height="13" fill="#fff" stroke="#8aa"/><path d="M1 1l10 7 10-7" fill="none" stroke="#8aa"/></svg>Email</li>
    <li>growing small towns</li><li>February gardening</li><li>55501234987650</li>
  </ul>
</footer>

</body>
</html>
```